Structural Engineering Firm Looking for High-Impact Lead Generation Focused Design (for B2B)

A well-established structural engineering firm in the UK wants a new website designed for them which will help them realise more business from online. Directly through the website as well as Ads and lead platforms. They need to compare favourably to competitors and have clarity. Current Site is here: http://www.marlowgrantpartners.example/ - you can take imagery from this site if you want to help with the design.
Updates

Target Market(s)

Homeowners, Architects, Designers, Construction Companies and Landlords

Industry/Entity Type

Professional Services

Number of Pages Required

5+ page

Font styles to use
Sans Serif

Requirements
Must have
• A Strong, Simple and Professional Design with a Focus on Lead Generation
Nice to have
• Creativity in the Detail, Clear Messaging
Should not have
• Too Much Colour, Too 'Consumer', Too Much Variation

```html
<!DOCTYPE html>
<html lang="en">
<head>
<meta charset="utf-8">
<title>Marlow Grant Partners – Structural Engineering</title>
<link rel="stylesheet" href="https://fonts.googleapis.com/css2?family=Jost:wght@400;500&display=swap">
<style>
:root{
  --cream:#fbf3e0;
  --ink:#1b1b1b;
  --mint:#7ee6c4;
  --mint-deep:#5fcfa9;
  --logo-grey:#3c3f3a;
  --white:#ffffff;
}
*{margin:0;padding:0;box-sizing:border-box}
html,body{width:1200px;height:2338px;overflow:hidden}
body{background:var(--cream);color:var(--ink);font-family:'Jost',sans-serif;position:relative}
h1,h2,h3,h4{font-weight:400}
.abs{position:absolute}

.brand{left:58px;top:58px;width:300px;white-space:nowrap;font-weight:500;color:var(--logo-grey);font-size:36px;line-height:46px;letter-spacing:-0.5px}
.nav{font-size:30px;line-height:38px}
.nav a{color:var(--ink);text-decoration:none;position:absolute;top:96px;white-space:nowrap}
.nav a.active{color:var(--mint)}
.nav .underline{position:absolute;left:552px;top:131px;width:104px;height:3px;background:var(--mint)}

.hero{left:58px;top:205px;width:1082px;height:544px;
  background:linear-gradient(180deg,#1f2b1f 0%,#2d3a2c 35%,#5a5446 62%,#6d5a3f 78%,#3e5a2c 100%);
  border:1px solid #8a8a8a}
.hero-text{left:121px;top:284px;width:800px;color:var(--white);font-size:28px;line-height:38.3px}
.hero-text .indent{padding-left:26px}

.section-title{left:0;width:1200px;text-align:center;font-size:46px;line-height:56px;font-weight:400}
.audience{top:891px;width:351px;height:367px}
.audience-label{width:100%;top:164px;text-align:center;color:var(--white);font-size:36px;line-height:40px}
.audience-label.active{color:var(--mint);text-decoration:underline;text-decoration-thickness:2px;text-underline-offset:4px}
.card-home{left:58px;background:linear-gradient(90deg,#5d6a6f 0%,#8c8f86 55%,#c7c2b8 65%,#6f6b66 100%)}
.card-design{left:425px;background:linear-gradient(180deg,#f4f3f0 0%,#e0ddd6 50%,#c9c4ba 100%)}
.card-contract{left:790px;background:linear-gradient(90deg,#eeeae2 0%,#d9cdb6 45%,#5a5650 80%,#2e2e2e 100%)}
.card-arrow{left:284px;top:325px}

.faq-q{left:64px;top:1428px;font-size:30px;line-height:38px}
.faq-h{left:118px;top:1501px;font-size:29px;line-height:36px;letter-spacing:1.5px}
.faq-p{left:61px;top:1547px;width:1060px;font-size:31px;line-height:38.4px}
.read-more{left:58px;top:1737px;width:225px;height:40px;border-radius:20px;background:var(--mint);
  box-shadow:3px 4px 5px rgba(0,0,0,.25);font-size:31px;line-height:40px;padding-left:40px;color:var(--ink);text-decoration:none}

.foot-h{top:1857px;font-size:29px;line-height:36px;letter-spacing:2px}
.contact-row{left:58px;display:flex;align-items:center;font-size:20px;line-height:26px}
.contact-row svg{flex:none}
.address{left:429px;font-size:20px;line-height:25px}
.foot-brand{left:822px;top:1862px;width:300px;white-space:nowrap;font-weight:500;color:var(--logo-grey);font-size:36px;line-height:46px;letter-spacing:-0.5px}

.legal{top:2207px;font-size:31px;line-height:38px;letter-spacing:1.5px;color:var(--ink);text-decoration:none}
.copyright{left:0;width:1206px;top:2262px;text-align:center;font-size:24px;line-height:30px}
</style>
</head>
<body>

<div class="abs brand">MARLOW GRANT<br>PARTNERS</div>

<nav class="nav">
  <a class="active" href="#" style="left:568px">Home</a>
  <a href="#" style="left:678px">About Us</a>
  <a href="#" style="left:843px">Projects</a>
  <a href="#" style="left:975px">Contact Us</a>
  <span class="underline"></span>
</nav>

<div class="abs hero" role="img" aria-label="Modern white house with timber deck and lit glazing at dusk, surrounded by trees"></div>
<p class="abs hero-text"><span class="indent">Established in 2008, Marlow Grant Partners is a</span><br>Structural Engineering and Party Wall Surveying<br>practice based in London and Sussex, covering all of<br>London and the Home Counties. We work alongside our<br>clients and their designers to find cost effective and<br>practical design solutions. You can rely on our<br>collaborative, approachable work ethic for every project.</p>

<h2 class="abs section-title" style="top:794px">We are there for</h2>

<a class="abs audience card-home" href="#" role="img" aria-label="Contemporary home extension with large glazed doors">
  <span class="abs audience-label active">Homeowners</span>
  <svg class="abs card-arrow" width="54" height="26" viewBox="0 0 54 26"><path d="M2 13H46M34 3L48 13L34 23" fill="none" stroke="var(--mint-deep)" stroke-width="5" stroke-linecap="round" stroke-linejoin="round"/></svg>
</a>
<a class="abs audience card-design" href="#" role="img" aria-label="Bright white kitchen and dining interior under a rooflight">
  <span class="abs audience-label">Designers</span>
</a>
<a class="abs audience card-contract" href="#" role="img" aria-label="Steel staircase with glass balustrade beside a brick wall">
  <span class="abs audience-label">Contractors</span>
</a>

<h2 class="abs section-title" style="top:1330px;width:1104px">FAQ</h2>

<p class="abs faq-q">An agency that can settle disputes between neighboring property owners ?</p>
<h3 class="abs faq-h">PARTY WALL ETC ACT 1996</h3>
<p class="abs faq-p">Are you planning an extension or alterations that could affect your neighbour’s property? If you are then it is highly likely the works fall under the Party Wall etc. Act 1996. The Act dictates what a property owner, whether residential or commercial, must do before commencing works on site.</p>
<a class="abs read-more" href="#">Read More</a>

<h4 class="abs foot-h" style="left:118px">GET IN TOUCH</h4>
<h4 class="abs foot-h" style="left:470px">SITE ADDRESS</h4>

<div class="abs contact-row" style="top:1921px">
  <svg width="34" height="30" viewBox="0 0 34 30"><circle cx="17" cy="15" r="13.5" fill="none" stroke="var(--ink)" stroke-width="2"/><path d="M11 8c-2 2-1 6 3 10s8 5 10 3l-3-3-2 1c-2-1-4-3-5-5l1-2z" fill="none" stroke="var(--ink)" stroke-width="2" stroke-linejoin="round"/></svg>
  <span style="margin-left:42px">+44 (0) 20 7946 0321</span>
</div>
<div class="abs contact-row" style="top:1970px">
  <svg width="34" height="30" viewBox="0 0 34 30"><circle cx="17" cy="15" r="13.5" fill="none" stroke="var(--ink)" stroke-width="2"/><path d="M11 8c-2 2-1 6 3 10s8 5 10 3l-3-3-2 1c-2-1-4-3-5-5l1-2z" fill="none" stroke="var(--ink)" stroke-width="2" stroke-linejoin="round"/></svg>
  <span style="margin-left:42px">+44 (0) 1632 960 417</span>
</div>
<div class="abs contact-row" style="top:2022px">
  <span style="font-size:36px;line-height:32px;width:34px">@</span>
  <span style="margin-left:10px">info@marlowgrantpartners.example</span>
</div>

<p class="abs address" style="top:1918px">Unit B4 Riverside Works<br>12 Hollins Lane<br>London SE1 7QX</p>
<p class="abs address" style="top:2018px;left:434px">Our Sussex Office is<br>Ashcombe West Sussex</p>

<div class="abs foot-brand">MARLOW GRANT<br>PARTNERS</div>

<a class="abs legal" href="#" style="left:240px">TERMS &nbsp;&amp; CONDITIONS</a>
<a class="abs legal" href="#" style="left:657px">PRIVACY POLICY</a>
<p class="abs copyright">Marlow Grant. Copyright © 2022. All rights reserved</p>

</body>
</html>
```